Photographic Tutorial website

We are looking for a fresh design for a photographic tutorial / workshop website. The website will have the included functions:

* Home (needs to have a login section)
* About Us
* Info about each course / workshop.
* Subscribe to courses and pay online.
* Members Area
* Photo gallery
* Contact us

The website will be implemented with our own made cms. We do not need it to be coded. We have a team ready to do this for us. We only need the PSD layout.

We have attached a mockup design that the client and I have come up with and we need the design to be taken to the next level.

Client also likes:
http://www.lumavistacamera.example/

Requirements
Must have
• Must Stand out i.e black backgrounds
Should not have
• Alter the logo in anyway.

```html
<!DOCTYPE html>
<html lang="en">
<head>
<meta charset="utf-8">
<title>Aperture Pals – Photographic Tuition</title>
<link href="https://fonts.googleapis.com/css2?family=Arimo:wght@400;700&display=swap" rel="stylesheet">
<style>
:root{
  --sky-top:#5b4a78;
  --sky-mid:#c98aa0;
  --sky-low:#e8a06a;
  --ground:#1a1410;
  --header-dark:#141414;
  --header-mid:#2a2a2a;
  --nav-dark:#252627;
  --nav-light:#3b3c3e;
  --rule:#6a6e72;
  --frame:#ffffff;
  --content-bg:#f4f4f4;
  --heading-blue:#2e6c9c;
  --body-text:#333333;
  --footer-text:#b5b5b5;
  --thumb-border:#c9c9c9;
  --label-bg:rgba(30,30,30,.72);
  --white:#ffffff;
}
*{box-sizing:border-box;margin:0;padding:0}
html,body{width:1200px;height:916px;overflow:hidden}
body{
  position:relative;
  font-family:"Arimo",Arial,sans-serif;
  background:linear-gradient(180deg,var(--sky-top) 0%,#8a6d96 25%,var(--sky-mid) 50%,var(--sky-low) 72%,#5a3a2e 86%,var(--ground) 100%);
}
.page{
  position:absolute;left:50px;top:52px;width:1104px;height:786px;
  background:var(--frame);padding:4px 4px 0 4px;
  box-shadow:0 0 18px rgba(0,0,0,.6);
}
.site-header{
  position:relative;height:101px;
  background:linear-gradient(180deg,var(--header-mid),var(--header-dark));
  border-bottom:3px solid var(--rule);
}
.brand{position:absolute;left:26px;top:30px;display:flex;align-items:center;gap:10px}
.brand-dot{width:34px;height:34px;border-radius:50%;background:#c8202a}
.brand-name{font-size:32px;font-weight:700;color:var(--white);letter-spacing:.5px}
.social{position:absolute;right:8px;top:0;display:flex}
.social a{width:45px;height:30px;border-left:1px solid #555;display:flex;align-items:center;justify-content:center}
.social .square{width:11px;height:11px;background:#d8d8d8;border-radius:2px}
.account{
  position:absolute;right:0;bottom:0;height:26px;padding:0 14px 0 40px;
  background:linear-gradient(180deg,#3a3a3a,#2c2c2c);
  clip-path:polygon(24px 0,100% 0,100% 100%,0 100%);
  font-size:11px;color:#e0e0e0;display:flex;align-items:center;gap:7px;
}
.account .sep{color:#888}
.main-nav{
  height:44px;display:flex;margin-top:2px;
  background:linear-gradient(180deg,var(--nav-light),var(--nav-dark));
  border-bottom:2px solid var(--rule);
}
.main-nav a{
  display:flex;align-items:center;justify-content:center;
  color:var(--white);font-size:13px;text-decoration:none;letter-spacing:.3px;
  border-right:1px solid #1a1a1a;box-shadow:1px 0 0 #4a4a4a;
}
.main-nav a:last-child{border-right:0;box-shadow:none}
.hero{display:flex;gap:4px;height:323px}
.hero-camera{flex:0 0 726px;background:radial-gradient(ellipse at 30% 45%,#e7a657 0%,#9a5a3c 30%,#3a2a30 70%,#1a1418 100%)}
.hero-tutor{flex:1;background:linear-gradient(135deg,#d8d8d6 0%,#b8b4ae 45%,#6e6862 100%)}
.content{
  display:flex;height:315px;background:var(--content-bg);padding:22px 0 0 0;
}
.col{font-size:12px;line-height:15.5px;color:var(--body-text)}
.col h2{font-size:17px;font-weight:400;color:var(--heading-blue);margin-bottom:15px}
.col h3{font-size:13px;font-weight:400;color:var(--heading-blue);margin-bottom:1px}
.col p{margin-bottom:15px}
.welcome{margin-left:27px;width:300px}
.updates{margin-left:57px;width:315px}
.gallery{margin-left:33px;width:360px}
.gallery h2{margin-bottom:10px}
.thumbs{display:grid;grid-template-columns:181px 181px;gap:8px 1px}
.thumb{
  width:179px;height:80px;border:1px solid var(--thumb-border);background:var(--white);padding:3px;
}
.thumb-img{position:relative;width:100%;height:100%}
.thumb-label{
  position:absolute;left:0;right:0;bottom:0;height:18px;background:var(--label-bg);
  color:var(--white);font-size:11px;font-weight:700;padding:3px 5px;
}
.wildlife{background:linear-gradient(135deg,#7a6a4e,#b08452 60%,#5a4a2a)}
.panorama{background:linear-gradient(180deg,#4c8cd0 0%,#dde6ee 45%,#2a7aa0 80%)}
.nightlights{background:linear-gradient(180deg,#1a1c34 0%,#46366a 50%,#c47a34 100%)}
.citywalks{background:linear-gradient(180deg,#8a8e96 0%,#c4c6ca 50%,#5a5c60 100%)}
.urban{background:linear-gradient(90deg,#b8352e 0%,#d8a88a 45%,#b9bcc2 100%)}
.nature{background:linear-gradient(180deg,#c6e08a 0%,#4c9a34 45%,#1e5a1a 100%)}
.site-footer{
  position:absolute;left:50px;top:838px;width:1104px;height:28px;
  background:linear-gradient(180deg,#3a3a3a,#1e1e1e);
  border-bottom:2px solid #555;
  font-size:11px;color:var(--footer-text);text-align:right;padding:7px 14px 0 0;
}
</style>
</head>
<body>
<div class="page">
  <header class="site-header">
    <div class="brand"><span class="brand-dot"></span><span class="brand-name">Aperture Pals</span></div>
    <nav class="social" aria-label="Social links">
      <a href="#"><span class="square"></span></a>
      <a href="#"><span class="square"></span></a>
      <a href="#"><span class="square"></span></a>
      <a href="#" aria-label="Email">
        <svg width="15" height="11" viewBox="0 0 15 11"><rect x="0.5" y="0.5" width="14" height="10" fill="#d8d8d8"/><path d="M0.5 0.5 L7.5 6 L14.5 0.5" fill="none" stroke="#2a2a2a" stroke-width="1.2"/></svg>
      </a>
    </nav>
    <div class="account"><span>Login</span><span class="sep">|</span><span>Register</span></div>
  </header>
  <nav class="main-nav">
    <a href="#" style="width:116px">HOME</a>
    <a href="#" style="width:116px">ABOUT</a>
    <a href="#" style="width:127px">COURSES</a>
    <a href="#" style="width:146px">SUBSCRIBE</a>
    <a href="#" style="width:142px">PAY ONLINE</a>
    <a href="#" style="width:170px">MEMBERS AREA</a>
    <a href="#" style="width:124px">GALLERY</a>
    <a href="#" style="width:155px">CONTACT</a>
  </nav>
  <section class="hero">
    <div class="hero-camera" role="img" aria-label="Camera on a tripod showing a city skyline on its screen, with warm blurred lights behind"></div>
    <div class="hero-tutor" role="img" aria-label="Photography tutor holding a camera beside a studio light"></div>
  </section>
  <main class="content">
    <section class="col welcome">
      <h2>Welcome to Aperture Pals</h2>
      <p>Warmest welcome to all the creatives out there!<br>Lorem ipsum dolor sit amet, consectetuer adipiscing elit, sed diam nonummy nibh.</p>
      <p>Lorem ipsum dolor sit amet, consectetuer adipiscing, sed diam nonummy nibh euismod tincidunt ut laoreet dolore magna aliquam erat volutpat. Ut wisi enim ad minim veniam, quis nostrud exerci tation ullamcorper suscipit lobortis nisl ut aliquip ex ea commodo sequat.</p>
      <p>Lorem ipsum dolor sit amet, consectetuer adipiscing elit, sed diam nonummy nibh euismod tincidunt ut laoreet dolore magna aliquam erat volutpat. Ut wisi enim ad minim veniam, quis nostrud exerci tation ullamcorper suscipit lobortis nisl ut aliquip ex modo.</p>
    </section>
    <section class="col updates">
      <h2>Latest Courses Updates</h2>
      <h3>Project Developments</h3>
      <p>Lorem ipsum dolor sit amet, consectetuer adipiscing elit, sed diam nonummy nibh euismod tincidunt ut laoreet dolore magna aliquam erat volutpat. Ut wisi enim ad minim veniam, quis nostrud exerci tation ullamcorper suscipit lobortis nisl ut aliquip ex ea commodo nsequat.</p>
      <h3>Night Lights in the City</h3>
      <p>Lorem ipsum dolor sit amet, consectetuer adipiscing elit, sed diam nonummy nibh euismod tincidunt ut laoreet dolore magna aliquam erat volutpat. Ut wisi enim ad minim veniam, quis nostrud exerci tation ullamcorper suscipit lobortis nisl ut aliquip ex ea commodo consequat. Duis autem vel eum iriure dolor in hendrerit in vulputate velit esse molestie consequat, vel illum.</p>
    </section>
    <section class="col gallery">
      <h2>Gallery</h2>
      <div class="thumbs">
        <div class="thumb"><div class="thumb-img wildlife" role="img" aria-label="Two antelopes in grassland"><span class="thumb-label">Wildlife</span></div></div>
        <div class="thumb"><div class="thumb-img panorama" role="img" aria-label="White seaside village under blue sky"><span class="thumb-label">Panorama</span></div></div>
        <div class="thumb"><div class="thumb-img nightlights" role="img" aria-label="City skyline lit up at night"><span class="thumb-label">Night Lights</span></div></div>
        <div class="thumb"><div class="thumb-img citywalks" role="img" aria-label="Curving urban overpass in grey light"><span class="thumb-label">City Walks</span></div></div>
        <div class="thumb"><div class="thumb-img urban" role="img" aria-label="Photographer with a camera on a city excursion"><span class="thumb-label">Urban Excursions</span></div></div>
        <div class="thumb"><div class="thumb-img nature" role="img" aria-label="Sunlit green forest"><span class="thumb-label">Nature</span></div></div>
      </div>
    </section>
  </main>
</div>
<footer class="site-footer">2012 © Aperture Pals | All rights reserved</footer>
</body>
</html>
```